Stationery Design Project

Hi All,

We need you to design stationary for a new Business and Accounting Advisory Firm. We have already got the logo designed and it is attached. If you could also if possible, match the fonts in your design to that on the logo’s provided.

What we need:
- Business Card
- A4 Letter head
- A4 Folders
- PPT template (Title page and regular page)

And what ever else you want to throw in.

We are in the process of getting the web site designed, however below is a list of websites which we like which will give you an understanding of the style that we are going for.

- plinvo.example
- brightmarrow.example
- tallyquill.example
- framelotus.example

I look forward to your seeing your design.
Updates

Hi All,

I have just realised that I forgot that i need to include a Bonded Ledgermen image on the letter head, please find attaced as File 1. Could you please have this image in the bottom left header.

Regards,

Morwen

Industry/Entity Type

Business

Requirements
Must have
• Outputs:
- Documents ready to print
- Generic editable information
- Pdf copies of the documents
- Word version of letterhead

```html
<!DOCTYPE html>
<html lang="en">
<head>
<meta charset="utf-8">
<title>Tarrow Partners – Stationery</title>
<link rel="stylesheet" href="https://fonts.googleapis.com/css2?family=Arimo:wght@400;700&display=swap">
<style>
  :root {
    --canvas: #e4e4e4;
    --paper: #ffffff;
    --card-front: #f4f5f6;
    --brand-blue: #2f5597;
    --brand-cyan: #3fb6d8;
    --brand-orange: #f7931e;
    --brand-yellow: #fbb83a;
    --ink: #555555;
    --ink-dark: #1d1d1b;
    --seal-red: #c4161c;
    --edge: #d6d6d6;
  }
  * { margin: 0; padding: 0; box-sizing: border-box; }
  html, body { width: 1200px; height: 1000px; overflow: hidden; }
  body {
    position: relative;
    background: var(--canvas);
    font-family: "Arimo", Arial, sans-serif;
    color: var(--ink);
  }
  .sheet {
    position: absolute;
    background: var(--paper);
    border: 1px solid var(--edge);
    overflow: hidden;
  }
  .letterhead { left: 214px; top: 75px; width: 607px; height: 858px; }
  .card-front { left: 719px; top: 387px; width: 284px; height: 141px; background: var(--card-front); }
  .card-back { left: 719px; top: 559px; width: 284px; height: 141px; }

  .brand { position: absolute; display: flex; align-items: center; gap: 9px; }
  .brand-dot {
    width: 30px; height: 30px; border-radius: 50%;
    background: var(--brand-cyan);
  }
  .brand-name {
    font-size: 18px; font-weight: 400; color: var(--brand-blue);
    white-space: nowrap;
  }
  .letterhead .brand { left: 42px; top: 42px; }
  .card-front .brand { left: 48px; top: 51px; }
  .card-front .brand-name { font-size: 17px; }

  .contact { position: absolute; font-size: 8.5px; line-height: 12px; }
  .contact-row { display: flex; }
  .contact-label { width: 14px; color: var(--brand-orange); }
  .contact-address { margin-top: 4px; padding-left: 14px; line-height: 11px; }
  .contact-web { padding-left: 14px; margin-top: 2px; color: var(--brand-orange); font-size: 9.5px; }
  .letterhead .contact { left: 441px; top: 51px; }

  .corner-field {
    position: absolute; left: 0; bottom: 0;
    background: linear-gradient(90deg, var(--brand-cyan) 0%, var(--brand-blue) 45%, var(--brand-yellow) 60%, var(--brand-orange) 100%);
    opacity: 0.9;
  }
  .letterhead .corner-field { width: 241px; height: 136px; }
  .card-back .corner-field { width: 136px; height: 76px; }

  .accreditation {
    position: absolute; left: 435px; top: 778px;
    display: flex; align-items: center; gap: 12px;
  }
  .accreditation-seal { width: 44px; height: 44px; border-radius: 50%; background: var(--seal-red); }
  .accreditation-name {
    font-size: 13px; font-weight: 700; line-height: 14px; color: var(--ink-dark);
  }

  .card-back .card-web {
    position: absolute; left: 21px; top: 14px;
    font-size: 9.5px; color: var(--brand-orange);
  }
  .card-back .card-address {
    position: absolute; left: 165px; top: 15px;
    font-size: 8.5px; line-height: 11px;
  }
  .card-back .contact { left: 151px; top: 77px; }
</style>
</head>
<body>

  <section class="sheet letterhead" aria-label="A4 letterhead">
    <div class="brand">
      <span class="brand-dot"></span>
      <span class="brand-name">Tarrow Partners</span>
    </div>

    <div class="contact">
      <div class="contact-row"><span class="contact-label">t</span><span>03 000 000</span></div>
      <div class="contact-row"><span class="contact-label">f</span><span>03 000 000</span></div>
      <div class="contact-row"><span class="contact-label">m</span><span>0400 000 000</span></div>
      <div class="contact-row"><span class="contact-label">e</span><span>xxxxx@xxxxxx.com.au</span></div>
      <div class="contact-address">14 Lorem Street, Aenean<br>Anriean VIC 3000</div>
      <div class="contact-web">www.xxxxxxxxxx.com.au</div>
    </div>

    <div class="corner-field" role="img" aria-label="Brand decoration area in blue and orange"></div>

    <div class="accreditation">
      <span class="accreditation-seal"></span>
      <span class="accreditation-name">Bonded<br>Ledgerman</span>
    </div>
  </section>

  <section class="sheet card-front" aria-label="Business card front">
    <div class="brand">
      <span class="brand-dot"></span>
      <span class="brand-name">Tarrow Partners</span>
    </div>
  </section>

  <section class="sheet card-back" aria-label="Business card back">
    <div class="card-web">www.xxxxxxx.com.au</div>
    <div class="card-address">14 Lorem Street, Aenean<br>Anriean VIC 3000</div>

    <div class="contact">
      <div class="contact-row"><span class="contact-label">t</span><span>03 000 000</span></div>
      <div class="contact-row"><span class="contact-label">f</span><span>03 000 000</span></div>
      <div class="contact-row"><span class="contact-label">m</span><span>0400 000 000</span></div>
      <div class="contact-row"><span class="contact-label">e</span><span>xxxxx@xxxxxx.com.au</span></div>
    </div>

    <div class="corner-field" role="img" aria-label="Brand decoration area in blue and orange"></div>
  </section>

</body>
</html>
```